Flyer for the Radiant Harvest Worship Day

I am looking to create a flyer for a one day prayer retreat our church is organizing.
This flyer will be posted on social media, websites and will also be printed so it can be mailed to people.
I am looking for something professional, with good use of our logo and band colors (logo colors).
I am counting on the designer's skill, creativity, art and knowledge of media communication to produce a flyer that will effectively and quickly convey the message we are trying to spread.
CONTENT OF THE FLYER:
Event title: Radiant Harvest Worship Day
Date: Tuesday July 2nd, 2019
Time: 11:00AM - 7:00PM
Belmont Hotel, 4875 Maple Ridge Road, Portland, Maine 04219 (Room: Evergreen)
Event Key words to highlight what the event is about: Prayer, Sharing the Word, Panel discussion, prophecy, Impartation.
Key phrases:
A one day prayer retreat.
Jesus Chris is Lord
Contact info:
www.tuvela.org
Phone: 207 583 2194
Email: contact@brookmeadow.org

```html
<!DOCTYPE html>
<html lang="en">
<head>
<meta charset="utf-8">
<title>Radiant Harvest Worship Day – Flyer</title>
<link rel="stylesheet" href="https://fonts.googleapis.com/css2?family=Oswald:wght@500&family=Playfair+Display:ital@1&family=Open+Sans:wght@400&display=swap">
<style>
  :root {
    --page: #ffffff;
    --navy: #16406f;
    --navy-deep: #103458;
    --title: #1b3a63;
    --orange: #f4a62a;
    --orange-shade: #c98a2a;
    --sky-light: #dfe7ef;
    --sky-mid: #9fb2c5;
    --sky-dark: #5f7891;
    --white: #ffffff;
  }
  * { margin: 0; padding: 0; box-sizing: border-box; }
  html, body { width: 1200px; height: 928px; overflow: hidden; background: var(--page); }

  .flyer {
    position: absolute; left: 306px; top: 82px;
    width: 588px; height: 764px; overflow: hidden;
    background: var(--sky-mid);
  }
  .hero-photo {
    position: absolute; inset: 0 0 auto 0; height: 520px;
    background:
      radial-gradient(ellipse 130px 260px at 50% 22%, rgba(255,255,255,.95), rgba(255,255,255,0) 70%),
      radial-gradient(ellipse 320px 140px at 45% 32%, rgba(255,255,255,.75), rgba(255,255,255,0) 70%),
      radial-gradient(ellipse 200px 90px at 30% 72%, rgba(170,215,230,.7), rgba(170,215,230,0) 70%),
      linear-gradient(180deg, var(--sky-dark) 0%, var(--sky-mid) 35%, var(--sky-light) 55%, var(--sky-mid) 80%, var(--sky-dark) 100%);
  }
  .shapes { position: absolute; inset: 0; }

  .frame {
    position: absolute; inset: 10px;
    border: 1.5px solid rgba(255,255,255,.7);
  }

  .brand {
    position: absolute; left: 396px; top: 44px;
    display: flex; align-items: center; gap: 8px;
    font-family: "Playfair Display", Georgia, serif; font-style: normal;
    font-size: 40px; color: var(--title); letter-spacing: 1px;
  }
  .brand-dot { width: 14px; height: 14px; border-radius: 50%; background: var(--orange); }

  .event-title {
    position: absolute; left: 0; right: 0; top: 132px;
    text-align: center;
    font-family: "Oswald", "Arial Narrow", sans-serif; font-weight: 500;
    font-size: 78px; line-height: 94px; letter-spacing: 1px;
    color: var(--title); text-transform: uppercase;
  }

  .tagline {
    position: absolute; left: 0; right: 0; top: 330px;
    text-align: center;
    font-family: "Playfair Display", Georgia, serif; font-style: italic;
    font-size: 26px; line-height: 30px; color: var(--white);
    text-shadow: 0 1px 3px rgba(0,0,0,.45);
  }

  .highlights {
    position: absolute; left: 380px; width: 200px; top: 420px;
    list-style: none; text-align: center;
    font-family: "Playfair Display", Georgia, serif; font-style: italic;
    font-size: 20px; line-height: 27px; color: var(--white);
  }

  .event-details {
    position: absolute; left: 42px; top: 562px;
    font-family: "Open Sans", Arial, sans-serif;
    font-size: 18px; line-height: 28px; color: var(--white);
  }
</style>
</head>
<body>
  <main class="flyer">
    <div class="hero-photo" role="img" aria-label="Photo of an open hand reaching up toward a glowing cross in the clouds"></div>

    <svg class="shapes" width="588" height="764" viewBox="0 0 588 764" aria-hidden="true">
      <polygon points="0,380 588,302 588,324 228,503" fill="rgba(22,64,111,.35)"/>
      <polygon points="228,503 588,324 588,644" fill="var(--orange)"/>
      <polygon points="228,503 588,644 588,686" fill="var(--orange-shade)"/>
      <polygon points="0,380 228,503 588,686 588,764 0,764" fill="var(--navy)"/>
      <polygon points="0,380 228,503 0,560" fill="var(--navy-deep)" opacity=".35"/>
    </svg>

    <div class="frame"></div>

    <div class="brand"><span class="brand-dot"></span>TUVELA</div>

    <h1 class="event-title">Radiant Harvest<br>Worship Day</h1>

    <p class="tagline">A one day prayer retreat.<br>Jesus Christ is Lord</p>

    <ul class="highlights">
      <li>Prayer</li>
      <li>Sharing the Word</li>
      <li>Panel discussion</li>
      <li>Prophecy</li>
      <li>Impartation</li>
    </ul>

    <p class="event-details">
      Date: Tuesday July 2nd, 2019<br>
      Time: 11:00AM - 7:00PM<br>
      Belmont Hotel, 4875 Maple Ridge<br>
      Road, Portland, Maine 04219<br>
      (Room: Evergreen)
    </p>
  </main>
</body>
</html>
```